Website Design for Freeze-Dried Food Manufacturing Company (Pet Food & Agri-Food)

We are looking for a high-level web designer to create a clean, modern, premium website design for Tarquel, a freeze-dried food manufacturing company operating in both the pet food and agri-food space.
This is not a basic website build β we are looking for a designer who understands brand positioning, layout, and user flow, not just visuals.
π― Project Objective
Design a website that:
Clearly communicates our capabilities and value proposition
Feels premium, credible, and product-driven
Guides users through a simple, intuitive journey
Clean and Crips
A critical requirement is clearly separating:
π Pet Food
π Agri-Food
These must feel like two distinct pathways within the same brand experience.
We have attached detailed documents outlining structure, layout, and messaging. These should be followed closely.
π What Success Looks Like
A high-impact homepage with strong visual hierarchy
Clear entry points into Pet Food and Agri-Food
Clean, intentional layout (not cluttered or template-like)
Thoughtful spacing, typography, and flow
A design that feels considered and elevated, not generic
π¨ Design Direction
We are aiming for a:
Minimal, premium aesthetic
Warm, natural color palette (creams, browns, muted tones)
Ingredient and product-focused visuals
Avoid:
Overly corporate / industrial styles
Generic SaaS-style layouts
Busy or over-designed interfaces
End Goal
A website that immediately communicates:
Who we are
What we do
Why weβre different
In a way that feels premium, clear, and easy to navigate.
Link to current website: https://tarquelfoods.example/
https://tarquelhealth.example/wp-admin/

```html
<!DOCTYPE html>
<html lang="en">
<head>
<meta charset="utf-8">
<title>Tarquel — Agri-Food</title>
<link href="https://fonts.googleapis.com/css2?family=Playfair+Display:wght@400;500&family=Poppins:wght@300;400;500;600&display=swap" rel="stylesheet">
<style>
:root{
  --cream:#f9f4ec;
  --cream-2:#f3ece2;
  --sand:#ece5dc;
  --sand-2:#e3dbd0;
  --sand-3:#dcd4ca;
  --brown:#3b2a20;
  --ink:#3a2d26;
  --copper:#c17a4c;
  --copper-dark:#a8623a;
  --rust:#b4714a;
  --muted:#6d5a4e;
  --white:#ffffff;
}
*{margin:0;padding:0;box-sizing:border-box}
html,body{width:1200px;height:4107px;overflow:hidden}
body{background:var(--cream);font-family:'Poppins',sans-serif;color:var(--ink);position:relative}
.abs{position:absolute}
.serif{font-family:'Playfair Display',serif}
.logo{font-family:'Poppins',sans-serif;font-weight:300;font-size:44px;color:var(--copper);letter-spacing:1px}
.nav-item{position:absolute;font-size:13px;font-weight:500;color:var(--brown);white-space:nowrap;z-index:3}
.nav-item.active{color:var(--copper);text-decoration:underline;text-underline-offset:4px}
.btn{display:flex;align-items:center;justify-content:center;border-radius:24px;background:var(--rust);color:var(--white);font-weight:600;font-size:15px;letter-spacing:.3px}
.btn-light{background:var(--white);color:var(--brown)}
.photo{border-radius:10px;box-shadow:0 8px 20px rgba(60,40,25,.18)}
.sec-title{left:0;width:1200px;text-align:center;font-family:'Playfair Display',serif;font-size:46px;color:var(--brown);letter-spacing:.5px}
.sec-rule{left:555px;width:90px;height:2px;background:var(--copper)}
.cat-label{text-align:center;font-size:20px;font-weight:500;color:var(--brown);line-height:31px}
.service{top:1618px;width:400px;height:300px;text-align:center}
.service h3{position:absolute;top:136px;width:100%;font-size:20px;font-weight:500;color:var(--brown)}
.service p{position:absolute;top:172px;left:0;right:0;margin:0 auto;font-size:17px;line-height:29px;color:var(--muted)}
.service svg{position:absolute;top:42px;left:165px}
.proc-label{font-size:17px;font-weight:500;color:var(--brown);text-align:center;width:200px}
.store-card{top:2862px;width:304px;height:378px;background:var(--cream);border-radius:22px;box-shadow:0 10px 28px rgba(70,45,25,.10);text-align:center}
.store-card .diamond{position:absolute;left:113px;top:60px;width:78px;height:78px;background:linear-gradient(135deg,#c8845a,#a15a33);border-radius:14px;transform:rotate(45deg)}
.store-card svg{position:absolute;left:128px;top:75px}
.store-card h3{position:absolute;top:176px;width:100%;font-size:19px;font-weight:500;color:var(--brown);line-height:29px}
.store-card .dot{position:absolute;top:236px;left:148px;width:8px;height:8px;border-radius:50%;background:var(--copper)}
.store-card p{position:absolute;top:262px;left:0;right:0;margin:0 auto;width:260px;font-size:16.5px;line-height:28px;color:var(--muted)}
.body-text{left:0;width:1200px;text-align:center;font-size:19px;line-height:30px;color:var(--brown)}
.foot-item{position:absolute;top:3970px;font-size:13px;font-weight:500;color:var(--brown);white-space:nowrap}
</style>
</head>
<body>

<!-- Hero image -->
<div class="abs" role="img" aria-label="Bowl of oat porridge topped with cinnamon crumble, apple slices and spices on a wooden table"
     style="left:698px;top:0;width:502px;height:590px;background:radial-gradient(circle at 62% 35%,#e9d6bd 0%,#b98a62 35%,#6b4a34 75%,#4a3224 100%);clip-path:polygon(74% 0,100% 0,100% 100%,35% 100%,0.8% 67.8%,0.8% 63.5%)"></div>

<!-- Header -->
<header>
  <div class="abs logo" style="left:108px;top:28px">Tarquel</div>
  <nav>
    <span class="nav-item" style="left:338px;top:55px">Home</span>
    <span class="nav-item" style="left:404px;top:55px">About</span>
    <span class="nav-item active" style="left:471px;top:55px">Applications</span>
    <span class="nav-item" style="left:581px;top:55px">Capabilities</span>
    <span class="nav-item" style="left:688px;top:55px">Quality &amp; Traceability</span>
    <span class="nav-item" style="left:857px;top:55px">Why Tarquel</span>
  </nav>
  <div class="abs btn" style="left:958px;top:42px;width:130px;height:46px;z-index:3">CONTACT</div>
</header>

<!-- Hero -->
<section class="hero">
  <div class="abs" style="left:111px;top:193px;width:3px;height:340px;background:var(--brown)"></div>
  <div class="abs" style="left:145px;top:231px;font-size:18px;color:var(--copper);letter-spacing:.5px">APPLICATIONS</div>
  <div class="abs" style="left:307px;top:243px;width:224px;height:1px;background:var(--copper)"></div>
  <h1 class="abs serif" style="left:145px;top:256px;font-weight:400;font-size:54px;line-height:64px;color:var(--brown)">Agri-Food</h1>
  <p class="abs" style="left:148px;top:328px;width:450px;font-size:18.5px;line-height:31px;color:var(--brown)">We work with agricultural and food partners to transform perishable inputs into stable, value-added products.</p>
  <div class="abs btn" style="left:147px;top:444px;width:186px;height:46px">START A PROJECT</div>
</section>

<!-- Categories -->
<section class="categories">
  <h2 class="abs sec-title" style="top:672px;font-weight:400">CATEGORIES</h2>
  <div class="abs sec-rule" style="top:740px"></div>

  <div class="abs photo" role="img" aria-label="Burlap sacks of powder in a rustic mill" style="left:155px;top:785px;width:427px;height:280px;background:linear-gradient(135deg,#4a3322,#a07a52 55%,#d1b48c)"></div>
  <div class="abs cat-label" style="left:155px;top:1088px;width:427px">POWDERS</div>

  <div class="abs photo" role="img" aria-label="Hands holding dry granules over a pile" style="left:617px;top:785px;width:427px;height:280px;background:linear-gradient(135deg,#8a6544,#c9a27a 50%,#e6cdb0)"></div>
  <div class="abs cat-label" style="left:617px;top:1088px;width:427px">GRANULES</div>

  <div class="abs photo" role="img" aria-label="Warehouse aisle with shelves of packaged goods and produce crates" style="left:155px;top:1153px;width:427px;height:280px;background:linear-gradient(135deg,#3d3128,#8e6f52 50%,#c9ad8b)"></div>
  <div class="abs cat-label" style="left:155px;top:1456px;width:427px">INCLUSIONS</div>

  <div class="abs photo" role="img" aria-label="Sunlit storehouse with wooden crates of oranges" style="left:617px;top:1153px;width:427px;height:280px;background:linear-gradient(135deg,#b4612c,#d79a62 45%,#eadcc8)"></div>
  <div class="abs cat-label" style="left:617px;top:1456px;width:427px">CUSTOM PROCESSED<br>FORMATS</div>
</section>

<!-- Services band -->
<section class="services">
  <div class="abs service" style="left:0;background:var(--sand)">
    <svg width="70" height="70" viewBox="0 0 70 70" fill="none" stroke="#c17a4c" stroke-width="2.2">
      <circle cx="35" cy="35" r="24"/><circle cx="35" cy="35" r="30" stroke-dasharray="6 4"/>
      <path d="M35 24l10 5v12l-10 5-10-5V29z M25 29l10 5 10-5 M35 34v12"/>
    </svg>
    <h3>OEM / PRIVATE LABEL</h3>
    <p style="width:340px">Custom product development from concept to commercialization</p>
  </div>
  <div class="abs service" style="left:400px;background:var(--sand-2)">
    <svg width="70" height="70" viewBox="0 0 70 70" fill="none" stroke="#c17a4c" stroke-width="2.2">
      <path d="M8 30L35 10l27 20v34H8z"/><rect x="16" y="32" width="30" height="26"/><rect x="50" y="34" width="6" height="22"/>
      <path d="M31 38v16M23 46h16M26 41l10 10M36 41L26 51"/>
    </svg>
    <h3>FREEZE DRYING</h3>
    <p style="width:310px">Industrial freeze-drying for food, ingredients, and agricultural products</p>
  </div>
  <div class="abs service" style="left:800px;background:var(--sand-3)">
    <svg width="70" height="70" viewBox="0 0 70 70" fill="none" stroke="#c17a4c" stroke-width="2.2">
      <path d="M24 40a15 15 0 1 1 22 0c-3 3-4 6-4 9H28c0-3-1-6-4-9z"/><path d="M28 54h14M30 59h10"/>
      <circle cx="35" cy="31" r="6"/><path d="M35 6v6M12 16l4 4M58 16l-4 4M6 32h6M58 32h6"/>
    </svg>
    <h3>R&amp;D TEST KITCHEN</h3>
    <p style="width:260px">Pilot runs, formulation, and product optimization</p>
  </div>
</section>

<!-- Process -->
<section class="process">
  <div class="abs" style="left:0;top:1918px;width:1200px;height:639px;background:linear-gradient(180deg,var(--cream) 0%,var(--cream-2) 45%,#ede4d9 100%)"></div>
  <h2 class="abs sec-title" style="top:2013px;font-weight:400">OUR PROCESS</h2>
  <div class="abs sec-rule" style="top:2080px"></div>

  <div class="abs proc-label" style="left:118px;top:2128px">DISCOVERY</div>
  <div class="abs proc-label" style="left:424px;top:2128px">R&amp;D</div>
  <div class="abs proc-label" style="left:730px;top:2128px">PRODUCTION</div>
  <div class="abs proc-label" style="left:271px;top:2444px">SOURCING</div>
  <div class="abs proc-label" style="left:577px;top:2444px">PILOT</div>
  <div class="abs proc-label" style="left:883px;top:2444px">PACKAGING</div>

  <svg class="abs" style="left:0;top:2140px" width="1200" height="320" viewBox="0 2140 1200 320">
    <defs>
      <linearGradient id="waveGrad" x1="0" x2="1">
        <stop offset="0" stop-color="#a35f38"/><stop offset=".5" stop-color="#c98559"/><stop offset="1" stop-color="#b36b40"/>
      </linearGradient>
    </defs>
    <g stroke="#c17a4c" stroke-width="2">
      <line x1="218" y1="2165" x2="218" y2="2210"/><line x1="524" y1="2165" x2="524" y2="2210"/><line x1="830" y1="2165" x2="830" y2="2210"/>
      <line x1="371" y1="2390" x2="371" y2="2435"/><line x1="677" y1="2390" x2="677" y2="2435"/><line x1="983" y1="2390" x2="983" y2="2435"/>
    </g>
    <g fill="#c17a4c">
      <circle cx="218" cy="2167" r="5"/><circle cx="524" cy="2167" r="5"/><circle cx="830" cy="2167" r="5"/>
      <circle cx="371" cy="2433" r="5"/><circle cx="677" cy="2433" r="5"/><circle cx="983" cy="2433" r="5"/>
    </g>
    <path d="M141 2300 A77 77 0 0 1 295 2300 A77 77 0 0 0 448 2300 A77 77 0 0 1 601 2300 A77 77 0 0 0 754 2300 A77 77 0 0 1 907 2300 A77 77 0 0 0 1060 2300"
          fill="none" stroke="url(#waveGrad)" stroke-width="24"/>
    <g fill="#f9f4ec" style="filter:drop-shadow(0 4px 8px rgba(80,50,30,.15))">
      <circle cx="218" cy="2300" r="62"/><circle cx="371" cy="2300" r="62"/><circle cx="524" cy="2300" r="62"/>
      <circle cx="677" cy="2300" r="62"/><circle cx="830" cy="2300" r="62"/><circle cx="983" cy="2300" r="62"/>
    </g>
    <g fill="none" stroke="#b5703f" stroke-width="2">
      <path d="M198 2328v-10a20 20 0 1 1 26-24"/><circle cx="224" cy="2296" r="9"/><circle cx="224" cy="2296" r="15" stroke-dasharray="4 3"/>
      <circle cx="371" cy="2300" r="26"/><path d="M371 2314v-30M371 2300c-8-2-12-8-12-14 8 0 12 6 12 14zM371 2296c8-2 12-8 12-14-8 0-12 6-12 14M347 2310c12-6 36-6 48 0"/>
      <circle cx="518" cy="2294" r="16"/><circle cx="518" cy="2294" r="7"/><path d="M530 2306l16 16M506 2318v10M516 2322v6"/>
      <rect x="660" y="2276" width="30" height="40" rx="3"/><path d="M667 2288h16M667 2296h16M667 2304h10"/><circle cx="690" cy="2314" r="8"/><path d="M686 2314l3 3 5-6"/>
      <circle cx="830" cy="2300" r="10"/><circle cx="830" cy="2300" r="17" stroke-dasharray="5 3"/><path d="M806 2292a26 26 0 0 1 44-12M854 2308a26 26 0 0 1-44 12"/>
      <path d="M963 2296l20-9 20 9v22l-20 9-20-9z M963 2296l20 9 20-9M983 2305v22"/><circle cx="983" cy="2280" r="8"/><path d="M979 2280l3 3 5-6"/>
    </g>
  </svg>
</section>

<!-- Storage -->
<section class="storage">
  <h2 class="abs sec-title" style="top:2662px;font-weight:400">STORAGE &amp; LOGISTICS</h2>
  <div class="abs sec-rule" style="top:2728px"></div>
  <p class="abs body-text" style="top:2760px;left:210px;width:780px">We provide integrated storage solutions to support product stability and supply chain continuity.</p>

  <div class="abs store-card" style="left:111px">
    <div class="diamond"></div>
    <svg width="48" height="48" viewBox="0 0 48 48" fill="none" stroke="#fff" stroke-width="2"><path d="M6 20L24 8l18 12v20H6z"/><rect x="13" y="22" width="22" height="16"/><path d="M24 24v12M18 30h12M20 26l8 8M28 26l-8 8"/></svg>
    <h3>COLD CHAIN<br>STORAGE</h3><div class="dot"></div>
    <p style="width:240px">Temperature-controlled environments for sensitive products</p>
  </div>
  <div class="abs store-card" style="left:449px">
    <div class="diamond"></div>
    <svg width="48" height="48" viewBox="0 0 48 48" fill="none" stroke="#fff" stroke-width="2"><path d="M8 40V10M40 40V10M8 18h32M8 30h32"/><rect x="14" y="20" width="8" height="10"/><rect x="24" y="32" width="10" height="8"/></svg>
    <h3>WAREHOUSE<br>STORAGE</h3><div class="dot"></div>
    <p style="width:230px">Scalable dry storage for finished goods and raw materials</p>
  </div>
  <div class="abs store-card" style="left:786px">
    <div class="diamond"></div>
    <svg width="48" height="48" viewBox="0 0 48 48" fill="none" stroke="#fff" stroke-width="2"><circle cx="24" cy="24" r="9"/><path d="M10 18a15 15 0 0 1 24-8M38 30a15 15 0 0 1-24 8M34 6v5h-5M14 42v-5h5"/></svg>
    <h3>CONTROLLED<br>ATMOSPHERE STORAGE</h3><div class="dot"></div>
    <p style="width:268px">Optimized conditions to maintain product quality and extend shelf life</p>
  </div>

  <p class="abs body-text" style="top:3295px;left:200px;width:800px">Integrated with production, our storage capabilities allow for seamless transition from processing to packaging and distribution.</p>
</section>

<!-- Call to action -->
<section class="cta">
  <div class="abs" role="img" aria-label="Industrial processing facility with grain piles, tinted in warm copper"
       style="left:0;top:3460px;width:1200px;height:430px;background:linear-gradient(180deg,#b9754b 0%,#c47f53 55%,#cd8a5c 100%)"></div>
  <h2 class="abs serif" style="left:0;top:3525px;width:1200px;text-align:center;font-weight:400;font-size:48px;line-height:57px;color:var(--white);letter-spacing:.5px">LET’S BUILD SOMETHING<br>TOGETHER</h2>
  <p class="abs" style="left:220px;top:3672px;width:760px;text-align:center;font-size:19px;line-height:31px;color:var(--white)">Tell us about your product, your category, and your timeline. We'll take it from concept to shelf.</p>
  <div class="abs btn btn-light" style="left:507px;top:3758px;width:186px;height:46px">START A PROJECT</div>
</section>

<!-- Footer -->
<footer>
  <div class="abs logo" style="left:108px;top:3947px">Tarquel</div>
  <nav>
    <span class="foot-item" style="left:365px">Home</span>
    <span class="foot-item" style="left:436px">About</span>
    <span class="foot-item" style="left:507px">Applications</span>
    <span class="foot-item" style="left:624px">Capabilities</span>
    <span class="foot-item" style="left:738px">Quality &amp; Traceability</span>
    <span class="foot-item" style="left:918px">Why Tarquel</span>
    <span class="foot-item" style="left:1032px">Contact</span>
  </nav>
  <div class="abs" style="left:110px;top:4023px;width:980px;height:1px;background:#e0d4c6"></div>
  <div class="abs" style="left:0;top:4050px;width:1200px;text-align:center;font-size:11px;color:var(--brown)">© 2026 ALL RIGHTS RESERVED</div>
  <div class="abs" style="left:966px;top:4040px;width:36px;height:36px;border-radius:50%;background:var(--rust)"></div>
  <div class="abs" style="left:1008px;top:4040px;width:36px;height:36px;border-radius:50%;background:var(--white)"></div>
  <div class="abs" style="left:1051px;top:4040px;width:36px;height:36px;border-radius:50%;background:var(--white)"></div>
</footer>

</body>
</html>
```